Event Graphics needed for Kid's Conference Event

I am in need of graphics for our event, Prairie Youngsters' Summit also known as TotMeet23. It is a conference event for elementary students - Kindergarten - 6th grade. The theme for the event is "Brickvale", playing off the imagery of Bloxo toys and Bloxo movies.
I need a title slide graphic as well as an 11x17 event poster. Title graphics should include sizes for social, 4x6 postcard, & 16x9 for projected screens. Graphic should include the following logo: the PQ RiseWave logo (this is our organization). Additionally, the poster should include the following information:
Millbrook Harvest Chapel
Millbrook, PQ
February 17-18
Guest Speaker: Dana Whitcomb, R/T National KidMin Director (see attached pictures; can be cropped as needed)
PrairieTotMeet.example

```html
<!DOCTYPE html>
<html lang="en">
<head>
<meta charset="utf-8">
<title>TotMeet23 – Event Poster</title>
<link rel="stylesheet" href="https://fonts.googleapis.com/css2?family=Fira+Sans:ital,wght@0,400;0,700;0,800;1,800&family=Lilita+One&family=Noto+Sans:wght@400;700&display=swap">
<style>
  :root {
    --yellow: #f6d550;
    --navy: #2d3790;
    --navy-deep: #1f2a78;
    --sky: #2cbdee;
    --ocean: #148bbb;
    --ocean-bright: #1a95c4;
    --charcoal: #232326;
    --gold-text: #f4dc6c;
    --white: #ffffff;
  }
  html, body {
    margin: 0;
    padding: 0;
    overflow: hidden;
    background: #ffffff;
  }
  .poster {
    position: relative;
    width: 776px;
    height: 1200px;
    overflow: hidden;
    background: var(--yellow);
    font-family: "Fira Sans", sans-serif;
  }
  .hero {
    position: absolute;
    left: 0; top: 0;
    width: 776px; height: 511px;
    background: radial-gradient(circle at 50% 50%, #f8da5a 0%, var(--yellow) 70%);
  }
  .hero-art {
    position: absolute;
    left: 0; top: 0;
  }
  .org-name {
    position: absolute;
    left: 0; width: 776px;
    top: 98px;
    text-align: center;
    font-family: "Fira Sans", sans-serif;
    font-weight: 800;
    font-size: 46px;
    line-height: 1;
    color: var(--navy);
    margin: 0;
  }
  .presents {
    position: absolute;
    left: 0; width: 776px;
    top: 203px;
    text-align: center;
    font-style: italic;
    font-weight: 800;
    font-size: 34px;
    letter-spacing: 1px;
    color: var(--navy);
    margin: 0;
  }
  .event-title {
    position: absolute;
    left: 0; width: 776px;
    top: 262px;
    text-align: center;
    font-family: "Lilita One", sans-serif;
    font-size: 70px;
    line-height: 1;
    letter-spacing: 1px;
    color: var(--navy);
    -webkit-text-stroke: 3px var(--white);
    paint-order: stroke fill;
    margin: 0;
  }
  .event-dates {
    position: absolute;
    left: 0; width: 800px;
    top: 368px;
    text-align: center;
    color: var(--navy);
    font-weight: 700;
    line-height: 1;
    margin: 0;
  }
  .event-dates .month { display: block; font-size: 48px; }
  .event-dates .days { display: block; font-size: 50px; margin-top: 4px; }

  .audience-band {
    position: absolute;
    left: 0; top: 511px;
    width: 776px; height: 79px;
    background: var(--ocean);
  }
  .audience-band p {
    margin: 0;
    line-height: 79px;
    text-align: center;
    color: var(--white);
    font-weight: 800;
    font-size: 22px;
    letter-spacing: 1.6px;
  }
  .band-corner {
    position: absolute;
    left: 0; top: 0;
  }

  .speaker-panel {
    position: absolute;
    left: 0; top: 590px;
    width: 776px; height: 290px;
    background: var(--charcoal);
  }
  .speaker-glow {
    position: absolute;
    left: 0; top: 27px;
    width: 480px; height: 230px;
    background: radial-gradient(ellipse at 55% 60%, #3a3a3e 0%, #2a2a2d 55%, var(--charcoal) 100%);
  }
  .speaker-photo {
    position: absolute;
    left: 58px; top: 27px;
    width: 277px; height: 230px;
    background: radial-gradient(ellipse at 45% 45%, #b5b5b5 0%, #7d7d7d 45%, #3c3c3f 100%);
  }
  .speaker-info {
    position: absolute;
    left: 339px; top: 70px;
    color: var(--gold-text);
    font-family: "Noto Sans", sans-serif;
  }
  .speaker-label { margin: 0; font-size: 29px; font-weight: 400; line-height: 1.1; }
  .speaker-name { margin: 10px 0 0; font-size: 41px; font-weight: 700; line-height: 1.1; }
  .speaker-role { margin: 6px 0 0 3px; font-size: 27px; font-weight: 400; line-height: 1.1; }

  .gallery {
    position: absolute;
    left: 0; top: 880px;
    width: 776px; height: 191px;
    background: var(--yellow);
  }
  .gallery-frame {
    position: absolute;
    border: 3px solid var(--navy-deep);
    border-radius: 5px;
    box-shadow: 2px 4px 8px rgba(0,0,0,0.35);
  }
  .frame-bricks {
    left: 37px; top: 4px; width: 232px; height: 180px;
    transform: rotate(-5deg);
    background: linear-gradient(135deg, #2f7fb0 0%, #3b8fbf 40%, #e0a040 70%, #2b6f9c 100%);
  }
  .frame-builders {
    left: 268px; top: -8px; width: 244px; height: 196px;
    transform: rotate(8deg);
    background: linear-gradient(120deg, #e8e3dc 0%, #f3d8d0 40%, #d9e9d0 70%, #f1e9e0 100%);
  }
  .frame-heart {
    left: 524px; top: 0px; width: 222px; height: 172px;
    transform: rotate(-3deg);
    background: linear-gradient(135deg, #eef1f4 0%, #c9a58a 35%, #5ea0d8 65%, #e8ecf0 100%);
  }

  .venue-band {
    position: absolute;
    left: 0; top: 1071px;
    width: 776px; height: 129px;
    background: var(--ocean-bright);
    text-align: center;
    color: var(--navy-deep);
    font-weight: 700;
  }
  .venue-band p {
    margin: 0;
    font-size: 33px;
    line-height: 40px;
    letter-spacing: 0.5px;
  }
  .venue-band .venue { padding-top: 18px; }
</style>
</head>
<body>
<main class="poster">

  <header class="hero">
    <svg class="hero-art" width="776" height="511" viewBox="0 0 776 511" aria-hidden="true">
      <circle cx="393" cy="262" r="227" fill="none" stroke="#ffffff" stroke-width="11" stroke-linecap="round" stroke-dasharray="0 27.5"/>
      <polygon class="ribbon-tail" points="145,200 106,355 192,355 192,252" fill="#148bbb"/>
      <polygon class="ribbon-tail" points="660,252 648,406 567,353" fill="#148bbb"/>
      <polygon class="ribbon-band" points="194,252 660,252 569,353 106,355" fill="#2cbdee"/>
    </svg>
    <p class="org-name">PQ RiseWave</p>
    <p class="presents">Presents</p>
    <h1 class="event-title">TOTMEET23</h1>
    <p class="event-dates"><span class="month">February</span><span class="days">17-18</span></p>
  </header>

  <section class="audience-band">
    <p>For elementary students | Kindergarten | 6th grade</p>
  </section>

  <section class="speaker-panel">
    <div class="speaker-glow"></div>
    <div class="speaker-photo" role="img" aria-label="Black and white portrait of guest speaker Dana Whitcomb"></div>
    <div class="speaker-info">
      <p class="speaker-label">Guest Speaker</p>
      <h2 class="speaker-name">Dana Whitcomb,</h2>
      <p class="speaker-role">R/T National KidMin Director</p>
    </div>
  </section>

  <svg class="band-corner" width="776" height="640" viewBox="0 0 776 640" aria-hidden="true" style="position:absolute;left:0;top:0;">
    <polygon points="0,464 0,511 48,511" fill="#148bbb"/>
    <polygon points="726,590 776,590 776,622" fill="#148bbb"/>
  </svg>

  <section class="gallery">
    <div class="gallery-frame frame-bricks" role="img" aria-label="Hands sorting colourful Bloxo bricks on a blue wooden table"></div>
    <div class="gallery-frame frame-builders" role="img" aria-label="Two girls building with pastel Bloxo bricks"></div>
    <div class="gallery-frame frame-heart" role="img" aria-label="Boy holding up a heart shape built from Bloxo bricks"></div>
  </section>

  <footer class="venue-band">
    <p class="venue">Millbrook Harvest Chapel Millbrook,PQ</p>
    <p class="register">Register at PrairieTotMeet.example</p>
  </footer>

</main>
</body>
</html>
```